KTV Catapult

I need a graphic package design for our new bodybuilding sports supplement. The artwork should be clean and useable for many formats. examples or great usage are www.brawnvelta.example, www.sinewcore.example and http://www.pellarynutrition.example/ as examples. I am adding our logo for your reference. The name Catapult is because it will help make "Big Guns" as a catch phrase, the product line will have other supplements such as creatine and protein powders and the artwork should be useable on all products. You can see our website for ideas at www.kestovalelabs.example
Updates

Hi everyone, There are some nice entries coming in. I do wonder if some of you are reading the brief as a few labels don't even highlight the product, KTV is the company, Catapult is the Product. Thanks Dex

Industry/Entity Type

Supplement

```html
<!DOCTYPE html>
<html lang="en">
<head>
<meta charset="utf-8">
<title>KTV Catapult Sports Supplement</title>
<link rel="stylesheet" href="https://fonts.googleapis.com/css2?family=Alfa+Slab+One&family=Quicksand:wght@700&family=Montserrat:wght@800&display=swap">
<style>
  :root {
    --red: #ed1c24;
    --red-dark: #c1171d;
    --red-light: #ef4136;
    --paper: #f1f1f3;
    --white: #ffffff;
    --slate: #58585a;
    --ink: #111111;
  }
  html, body {
    margin: 0;
    padding: 0;
    overflow: hidden;
    background: var(--white);
  }
  .label {
    position: relative;
    width: 1200px;
    height: 848px;
    overflow: hidden;
    background: var(--white);
  }
  .backdrop {
    position: absolute;
    inset: 0;
    width: 1200px;
    height: 848px;
    display: block;
  }
  .brand-mark {
    position: absolute;
    top: 48px;
    left: 0;
    width: 1200px;
    margin: 0;
    text-align: center;
    font-family: "Montserrat", sans-serif;
    font-weight: 800;
    font-size: 58px;
    letter-spacing: 2px;
    line-height: 1;
    color: var(--ink);
  }
  .product-name {
    position: absolute;
    top: 376px;
    left: 0;
    width: 1200px;
    margin: 0;
    text-align: center;
    font-family: "Alfa Slab One", serif;
    font-weight: 400;
    font-size: 62px;
    line-height: 1;
    letter-spacing: 3px;
    color: var(--red-dark);
  }
  .product-type {
    position: absolute;
    top: 447px;
    left: 0;
    width: 1200px;
    margin: 0;
    text-align: center;
    font-family: "Quicksand", sans-serif;
    font-weight: 700;
    font-size: 38px;
    line-height: 1;
    color: var(--ink);
  }
  .benefits {
    position: absolute;
    top: 552px;
    left: 0;
    width: 1200px;
    margin: 0;
    padding: 0;
    list-style: none;
    text-align: center;
    font-family: "Quicksand", sans-serif;
    font-weight: 700;
    font-size: 28px;
    line-height: 50px;
    color: var(--white);
  }
  .website {
    position: absolute;
    top: 774px;
    left: 0;
    width: 1200px;
    margin: 0;
    text-align: center;
    font-family: "Quicksand", sans-serif;
    font-weight: 700;
    font-size: 14px;
    color: var(--white);
  }
</style>
</head>
<body>
  <main class="label">
    <svg class="backdrop" viewBox="0 0 842 595" preserveAspectRatio="none">
      <defs>
        <linearGradient id="red-field-tone" x1="0" y1="0" x2="1" y2="1">
          <stop offset="0" stop-color="var(--red-light)"/>
          <stop offset="0.5" stop-color="var(--red)"/>
          <stop offset="1" stop-color="var(--red-dark)"/>
        </linearGradient>
      </defs>
      <rect class="red-field" x="0" y="0" width="842" height="340" fill="url(#red-field-tone)" role="img" aria-label="Angular red banding behind the brand name"/>
      <polygon class="brand-notch" points="150,0 428,118 690,0" fill="var(--paper)" aria-hidden="true"/>
      <polygon class="name-band" points="0,320 428,232 842,320 842,440 428,358 0,452" fill="var(--white)" aria-hidden="true"/>
      <polygon class="base-slate" points="0,460 428,364 842,448 842,595 0,595" fill="var(--slate)" aria-hidden="true"/>
    </svg>

    <div class="brand-mark">KTV</div>

    <h1 class="product-name">CATAPULT</h1>
    <p class="product-type">Sports Supplement</p>

    <ul class="benefits">
      <li>Advanced Formula</li>
      <li>Boostes Energy</li>
      <li>Maintains Blood Flow</li>
      <li>Guliten Free</li>
    </ul>

    <p class="website">www.kestovalelabs.example</p>
  </main>
</body>
</html>
```